Harwell Church Yuletide Recital 2013

Create a 18x22 inch poster for an upcoming church concert event with the following details:
Theme: Jesus Is Coming Again
Date:12/21/13 Time: 10:40am
Featuring the Choirs of the Harwell Church and special guests.
Harwell FGB Church
415-36 92nd Terrace,
Laurelton, NY 10987
Pastor Desmond K. Halloway
The target audience is predominantly african-american
The concert theme has been changed to: "Jesus The Light of the World"
Church

```html
<!DOCTYPE html>
<html lang="en">
<head>
<meta charset="utf-8">
<title>Harwell Church Yuletide Recital 2013</title>
<link rel="stylesheet" href="https://fonts.googleapis.com/css2?family=Bodoni+Moda:wght@700&family=Courier+Prime&display=swap">
<style>
  :root {
    --bg: #0d0c0c;
    --bg-edge: #050505;
    --ink-light: #f4f2ee;
    --ink-red: #a3100f;
    --ink-date: #8e1512;
    --ink-soft: #d8d4cc;
    --guitar-wood: #5a1410;
    --guitar-glow: #c0735a;
  }
  html, body {
    margin: 0;
    padding: 0;
    overflow: hidden;
    background: var(--bg-edge);
  }
  .poster {
    position: relative;
    width: 843px;
    height: 1200px;
    overflow: hidden;
    background: radial-gradient(ellipse at 45% 40%, #1a1818 0%, var(--bg) 55%, var(--bg-edge) 100%);
  }
  .headline {
    position: absolute;
    top: 128px;
    left: 50%;
    margin: 0;
    font-family: "Bodoni Moda", serif;
    font-weight: 700;
    font-size: 84px;
    line-height: 1.1;
    letter-spacing: -1px;
    white-space: nowrap;
    transform: translateX(-50%) scaleX(0.6);
    transform-origin: center;
  }
  .headline-name { color: var(--ink-light); }
  .headline-rest { color: var(--ink-red); }
  .event-type {
    position: absolute;
    top: 455px;
    left: 0;
    width: 850px;
    margin: 0;
    text-align: center;
    font-family: "Courier Prime", monospace;
    font-weight: 400;
    font-size: 53px;
    line-height: 1;
    color: var(--ink-light);
  }
  .featuring {
    position: absolute;
    top: 540px;
    left: 0;
    width: 850px;
    margin: 0;
    text-align: center;
    font-family: "Courier Prime", monospace;
    font-size: 21px;
    line-height: 30px;
    color: var(--ink-soft);
  }
  .guitar-photo {
    position: absolute;
    left: 110px;
    top: 680px;
    width: 320px;
    height: 520px;
    background:
      radial-gradient(ellipse 38% 14% at 47% 45%, var(--guitar-glow) 0%, #6e2a1d 45%, transparent 100%),
      radial-gradient(ellipse 55% 40% at 48% 55%, var(--guitar-wood) 0%, #2a0b09 60%, transparent 100%);
  }
  .when {
    position: absolute;
    top: 936px;
    left: 462px;
    width: 266px;
    text-align: center;
    font-family: "Courier Prime", monospace;
    font-size: 38px;
    line-height: 58px;
    color: var(--ink-date);
  }
  .where {
    position: absolute;
    top: 1072px;
    right: 3px;
    width: 510px;
    text-align: center;
    font-family: "Courier Prime", monospace;
    font-size: 23px;
    line-height: 36px;
    color: var(--ink-soft);
    white-space: nowrap;
  }
  .where p { margin: 0; }
</style>
</head>
<body>
  <main class="poster">
    <h1 class="headline"><span class="headline-name">Jesus</span> <span class="headline-rest">The Light of the World</span></h1>

    <p class="event-type">church concert</p>
    <p class="featuring">Featuring the Choirs of the Harwell Church<br>and special guests</p>

    <div class="guitar-photo" role="img" aria-label="Close-up photograph of an acoustic guitar seen along its neck, strings and sound hole lit in warm red tones"></div>

    <div class="when">
      <div class="when-date">21 dec 2013</div>
      <div class="when-time">10:40am</div>
    </div>

    <div class="where">
      <p class="where-venue">Harwell FGB Church</p>
      <p class="where-street">415-36 92nd Terrace, Laurelton,</p>
      <p class="where-city">NY 10987 Pastor Desmond K. Halloway</p>
    </div>
  </main>
</body>
</html>
```